We need a flyer design for a new fencing business. We do ferrowane fencing instalations and pride our company on Reliabilty, Dependabilty and genuine quality. Because it's not just a fence... It's your fence. Our company offers customer free quotes. Things that would need to be on the flyer;

*Company Name - Valley Copperpath Fencing
*Company email - copperpathfencing@quillmail.net
*Company Phone number - 0455 912 307

*Ferrowane fence specialist
*Free quotes

```html
<!DOCTYPE html>
<html lang="en">
<head>
<meta charset="utf-8">
<title>Valley Copperpath Fencing – Flyer</title>
<link href="https://fonts.googleapis.com/css2?family=Anton&family=Archivo+Black&display=swap" rel="stylesheet">
<style>
  :root {
    --paper: #ffffff;
    --ink: #0a0a0a;
    --frame-blue: #1a2fd6;
    --frame-dark: #0b1680;
    --accent-blue: #1224c8;
    --stamp-red: #7e1414;
    --timber-light: #d9b27a;
    --timber-mid: #c49a5e;
    --timber-dark: #a87c45;
  }
  * { margin: 0; padding: 0; box-sizing: border-box; }
  html, body { width: 846px; height: 1200px; overflow: hidden; background: var(--paper); }
  .flyer {
    position: relative;
    width: 846px;
    height: 1200px;
    background: var(--paper);
    border: 6px solid var(--frame-blue);
    box-shadow: inset 0 0 0 2px var(--frame-dark), inset 0 0 14px 4px rgba(11, 22, 128, 0.55);
    overflow: hidden;
  }
  .brand-title {
    position: absolute;
    top: 22px; left: 0; width: 100%;
    text-align: center;
    font-family: "Archivo Black", sans-serif;
    font-size: 41px;
    letter-spacing: 2px;
    color: var(--ink);
    white-space: nowrap;
  }
  .fence-photo {
    position: absolute;
    top: 97px; left: 142px;
    width: 548px; height: 471px;
    background: linear-gradient(180deg, var(--timber-light), var(--timber-mid) 55%, var(--timber-dark));
  }
  .stamp {
    position: absolute;
    top: 325px; left: 420px;
    transform: translate(-50%, -50%) rotate(-45deg);
    text-align: center;
    font-family: "Archivo Black", sans-serif;
    font-size: 47px;
    line-height: 1.05;
    letter-spacing: 2px;
    color: var(--stamp-red);
    white-space: nowrap;
    opacity: 0.92;
  }
  .pitch {
    position: absolute;
    top: 632px; left: 50%;
    transform: translateX(-50%) scaleX(0.5);
    transform-origin: center top;
    text-align: center;
    font-family: "Anton", sans-serif;
    font-size: 60px;
    line-height: 86px;
    color: var(--ink);
    white-space: nowrap;
  }
  .specialty {
    position: absolute;
    top: 933px; left: 0; width: 100%;
    text-align: center;
    font-family: "Archivo Black", sans-serif;
    font-size: 33px;
    letter-spacing: 4px;
    color: var(--accent-blue);
    white-space: nowrap;
  }
  .contact {
    position: absolute;
    left: 0; width: 100%;
    text-align: center;
    font-family: "Archivo Black", sans-serif;
    color: var(--ink);
    white-space: nowrap;
  }
  .contact-email { top: 1072px; font-size: 30px; letter-spacing: 2px; }
  .contact-phone { top: 1130px; font-size: 35px; letter-spacing: 5px; }
</style>
</head>
<body>
  <main class="flyer">
    <h1 class="brand-title">VALLEY COPPERPATH FENCING</h1>

    <div class="fence-photo" role="img" aria-label="Photo of a plain timber lap fence panel"></div>
    <p class="stamp">FENCE LACKING<br>INSPIRATION?</p>

    <p class="pitch">Is your fence lacking inspiration? Valley copperpath fencing<br>can help!! Call now for your FREE quote</p>

    <p class="specialty">FERROWANE SPECIALISTS</p>

    <p class="contact contact-email">copperpathfencing@quillmail.net</p>
    <p class="contact contact-phone">0455912307</p>
  </main>
</body>
</html>
```